Lumora Works - Design & Marketing Website Re-branding

UPDATE:
We are working on finalizing our color palette but are hoping that the designers will guide us to the right choice of colors by looking at our color inspiration file that we just uploaded and lead us in the right direction.

-----

I am exploring new design inspiration for a re-branding of my website. My current website is old and outdated and I lack the time to design it myself in addition to the fact that I am my own worst client.

I do website design, development and marketing as well as some SEO consulting and business development for small to mid-size companies in a range of industries.

https://lumoraworks.example

I like clean modern designs without cartoon images. The brands I'm going after are looking for a professional look and feel. I need something that shows my many years of being in business that is very professional.

I prefer minimal use of color. Mostly black and white with maybe one or two other colors. I am open to the suggestions by the designer.

Target Market(s)

Small to mid-size companies

Industry/Entity Type

Website Design, SEO and Markeitng

Number of Pages Required

4 page

Font styles to use
Sans Serif

Requirements
Must have
• Must be clean, modern and professional - I am not a huge fan of a lot of color and I'm open to new color suggestions by the designer
Nice to have
• A good balance of whitespace to content and graphics
Should not have
• Please no people illustrations

```html
<!DOCTYPE html>
<html lang="en">
<head>
<meta charset="utf-8">
<title>Lumora Works — Design &amp; Marketing</title>
<link href="https://fonts.googleapis.com/css2?family=Roboto+Condensed:wght@400;500;600&family=Roboto:wght@400;500;700&family=Outfit:wght@400;500;600&display=swap" rel="stylesheet">
<style>
:root{
  --ink:#111;
  --text:#222;
  --muted:#444;
  --accent:#9a4f1c;
  --blue:#1c5fd8;
  --soft:#f2f2f2;
  --dark:#0b0b0b;
  --line:#e4e4e4;
  --white:#fff;
}
*{box-sizing:border-box;margin:0;padding:0}
html,body{width:1200px;height:3966px;overflow:hidden}
body{font-family:"Roboto",Arial,sans-serif;color:var(--text);background:var(--white);position:relative}
.abs{position:absolute}
h2.section-title{font-family:"Roboto Condensed",sans-serif;font-weight:500;font-size:34px;color:var(--ink);text-align:center}
.tick{position:absolute;width:2px;height:26px;background:var(--accent)}
.btn-outline{position:absolute;border:2px solid var(--accent);border-radius:20px;font:500 12px "Roboto",sans-serif;color:var(--ink);display:flex;align-items:center;justify-content:center;background:#fff}

/* hero */
.hero{position:absolute;left:0;top:0;width:1200px;height:557px;background:linear-gradient(100deg,#2a2622 0%,#4d4a44 40%,#7b7468 70%,#3a3630 100%)}
.hero-shade{position:absolute;inset:0;background:linear-gradient(90deg,rgba(0,0,0,.55),rgba(0,0,0,.15) 70%,rgba(0,0,0,.1))}
.brand{position:absolute;left:142px;top:16px;font:600 28px "Outfit",sans-serif;color:#fff}
.nav{position:absolute;top:22px;right:141px;display:flex;align-items:center;gap:32px;font:500 12px "Outfit",sans-serif;color:#fff}
.nav .pill{background:#fff;color:var(--blue);border-radius:18px;padding:9px 20px;margin-left:20px}
.badge{position:absolute;left:142px;top:172px;border:1.5px solid #fff;padding:8px 16px;font:400 13px "Outfit",sans-serif;color:#fff;letter-spacing:.3px}
.hero h1{position:absolute;left:142px;top:218px;font:600 43px/58px "Outfit",sans-serif;color:#fff;width:520px}
.hero .lead{position:absolute;left:142px;top:350px;font:400 15px "Outfit",sans-serif;color:#fff}
.hero .btn-blue{position:absolute;left:142px;top:398px;width:104px;height:34px;border-radius:17px;background:var(--blue);color:#fff;font:500 12px "Outfit",sans-serif;display:flex;align-items:center;justify-content:center}
.hero .phone{position:absolute;left:268px;top:406px;color:#fff;font:400 14px "Outfit",sans-serif;display:flex;gap:10px;align-items:center}
.avatars{position:absolute;left:142px;top:460px;display:flex}
.avatars span{width:34px;height:34px;border-radius:50%;border:2px solid #fff;background:#8d7a6a;margin-right:-8px}
.hero .happy{position:absolute;left:236px;top:462px;color:#fff;font:400 12px/16px "Outfit",sans-serif}

/* about */
.about h2{position:absolute;left:142px;top:714px;font:500 35px/46px "Roboto Condensed",sans-serif;color:var(--ink)}
.about p{position:absolute;left:142px;width:400px;font-size:12px;line-height:23px;color:var(--text)}
.photo{position:absolute;border-radius:8px}

/* services */
.card{position:absolute;width:441px;height:246px;background:#fff;border-radius:6px;box-shadow:0 2px 14px rgba(0,0,0,.08);padding:0 21px}
.card svg{position:absolute;left:21px;top:34px}
.card h3{position:absolute;left:21px;top:95px;font:500 21px "Roboto Condensed",sans-serif;color:var(--ink)}
.card p{position:absolute;left:21px;top:132px;width:395px;font-size:12px;line-height:23px}
.card .btn-outline{left:21px;top:191px;width:119px;height:36px}

/* reviews */
.reviews{position:absolute;left:0;top:1903px;width:1200px;height:459px;background:var(--soft)}
.review{position:absolute;width:280px;text-align:center;font-size:12px;line-height:23px}
.review .face{width:78px;height:78px;border-radius:50%;background:linear-gradient(#c9c3bb,#8a8178);margin:0 auto 12px}
.review .who{font-weight:500;margin-top:16px}
.arrow{position:absolute;width:30px;height:30px;border:1.5px solid var(--ink);border-radius:50%;display:flex;align-items:center;justify-content:center}

/* stats */
.stats{position:absolute;left:0;top:2362px;width:1200px;height:168px;background:linear-gradient(90deg,#151515,#2b2b2b 50%,#111)}
.stat{position:absolute;top:52px;width:200px;text-align:center;color:#fff}
.stat b{display:block;font:500 38px "Roboto Condensed",sans-serif}
.stat span{font-size:12px}
.vline{position:absolute;top:52px;width:1px;height:62px;background:#555}

/* blog */
.post{position:absolute;top:2732px;width:282px}
.post .img{height:186px;border-radius:2px}
.post h4{font:500 16px/21px "Roboto Condensed",sans-serif;color:var(--ink);margin-top:18px;height:44px}
.post p{font-size:12px;line-height:23px;margin-top:14px;height:72px}
.post .meta{font-size:12px;margin-top:8px}
.post .more{display:inline-block;margin-top:22px;font-size:12px;font-weight:500;color:var(--ink);text-decoration:underline}

/* clients */
.client{position:absolute;top:3434px;width:173px;height:96px;background:#fff;box-shadow:0 2px 12px rgba(0,0,0,.09);display:flex;align-items:center;justify-content:center;font:600 16px "Roboto",sans-serif;color:#333;gap:8px;text-align:center}

/* footer */
.footer{position:absolute;left:0;top:3600px;width:1200px;height:366px;background:var(--dark);color:#fff}
.footer h5{position:absolute;top:78px;font:500 17px "Roboto Condensed",sans-serif}
.footer ul{position:absolute;list-style:none;font-size:12px;line-height:33px}
.footer ul li::before{content:"›";margin-right:12px}
.fitem{position:absolute;display:flex;gap:14px;font-size:12px;line-height:19px}
.ficon{width:28px;height:28px;border:1.5px solid #fff;border-radius:50%;flex:none}
.footer-brand{position:absolute;right:141px;top:150px;font:600 26px "Outfit",sans-serif;color:#fff}
.footer .rule{position:absolute;left:142px;top:316px;width:918px;height:1px;background:#444}
.footer .legal{position:absolute;top:336px;font-size:12px}
</style>
</head>
<body>

<section class="hero">
  <div class="hero-shade" role="img" aria-label="Team collaborating in a bright office, whiteboard with project sketches"></div>
  <div class="brand">Lumora Works</div>
  <nav class="nav"><span>Home</span><span>About Us</span><span>Services</span><span>Blog</span><span class="pill">Contact Us</span></nav>
  <div class="badge">WELCOME TO LUMORA WORKS</div>
  <h1>Every Business Has A Story. We Help You Tell It.</h1>
  <div class="lead">Compelling website experiences that elevate your business.</div>
  <div class="btn-blue">Learn More</div>
  <div class="phone"><svg width="15" height="15" viewBox="0 0 24 24"><path fill="#fff" d="M6.6 10.8a15 15 0 0 0 6.6 6.6l2.2-2.2c.3-.3.7-.4 1-.2 1.1.4 2.3.6 3.6.6.6 0 1 .4 1 1V20c0 .6-.4 1-1 1A17 17 0 0 1 3 4c0-.6.4-1 1-1h3.5c.6 0 1 .4 1 1 0 1.3.2 2.5.6 3.6.1.3 0 .7-.2 1z"/></svg>123-456-7890</div>
  <div class="avatars" role="img" aria-label="Customer portraits"><span></span><span style="background:#6b5a4c"></span><span style="background:#a08a78"></span></div>
  <div class="happy">200+ Happy<br>Customers</div>
</section>

<section class="about">
  <div class="tick" style="left:142px;top:680px"></div>
  <h2>We Create Websites That<br>Inspire</h2>
  <p style="top:816px">We Are A Collaborative Team Of Word Nerds, Choreographers Of Shapes &amp; Ideas, Ambassadors Of Data, Content Warriors And Inspirational Conversationalists Ready To Help You No Matter Where You Are In Your Journey.</p>
  <p style="top:913px">We Have A Deep Understanding Of What It Takes To Grow A Business And We Collaborate With You Every Step Of The Way From Strategy To Implementation And Beyond.</p>
  <div class="btn-outline" style="left:142px;top:999px;width:104px;height:34px">Contact Us</div>
  <svg class="abs" style="left:600px;top:600px" width="580" height="500" viewBox="0 0 580 500">
    <circle cx="315" cy="255" r="240" fill="none" stroke="#ececec" stroke-width="1.5"/>
    <circle cx="315" cy="255" r="175" fill="none" stroke="#ececec" stroke-width="1.5"/>
    <g fill="#8a4a1c"><circle cx="311" cy="20" r="5"/><circle cx="510" cy="117" r="5"/><circle cx="471" cy="217" r="5"/><circle cx="551" cy="285" r="5"/><circle cx="481" cy="368" r="5"/><circle cx="389" cy="483" r="5"/><circle cx="245" cy="440" r="5"/></g>
  </svg>
  <div class="photo" style="left:760px;top:673px;width:298px;height:339px;background:linear-gradient(135deg,#c98a3a,#e8e4dc 55%,#b9b5ad)" role="img" aria-label="Designer reviewing website wireframes at a desk with colour swatches"></div>
  <div class="photo" style="left:608px;top:858px;width:205px;height:189px;background:linear-gradient(160deg,#d9dde2,#6e757c 60%,#2c2f33);box-shadow:0 4px 16px rgba(0,0,0,.15)" role="img" aria-label="Laptop showing a development dashboard"></div>
</section>

<section class="services">
  <div class="tick" style="left:599px;top:1183px"></div>
  <h2 class="section-title abs" style="left:0;width:1200px;top:1218px">Our Services</h2>

  <div class="card" style="left:142px;top:1289px">
    <svg width="42" height="40" viewBox="0 0 42 40" fill="none" stroke="#222" stroke-width="1.6"><rect x="2" y="2" width="32" height="26" rx="2"/><path d="M2 9h32M8 15l-3 3 3 3M14 15l3 3-3 3"/><circle cx="32" cy="30" r="6"/><circle cx="32" cy="30" r="2"/></svg>
    <h3>Websites Simplified</h3>
    <p>A Complete End-To-End Website Subscription Solution That Propels Your Business Forward.</p>
    <div class="btn-outline">Read More</div>
  </div>
  <div class="card" style="left:618px;top:1289px">
    <svg width="42" height="40" viewBox="0 0 42 40" fill="none" stroke="#222" stroke-width="1.6"><rect x="2" y="2" width="38" height="28" rx="2"/><path d="M12 38h18M21 30v8M14 22l14-14 3 3-14 14h-3z"/></svg>
    <h3>Custom Website Design</h3>
    <p>Blending The Best Principles Of Design, Data And Functionality To Express Your Brand.</p>
    <div class="btn-outline">Read More</div>
  </div>
  <div class="card" style="left:142px;top:1571px">
    <svg width="42" height="44" viewBox="0 0 42 44" fill="none" stroke="#222" stroke-width="1.6"><rect x="2" y="2" width="38" height="40" rx="2"/><path d="M2 9h38"/><circle cx="21" cy="26" r="10"/><circle cx="21" cy="26" r="4"/></svg>
    <h3>Website Support</h3>
    <p>Reliable Top Tier SiteCraft Website Support, Maintenance And Hosting,</p>
    <div class="btn-outline">Read More</div>
  </div>
  <div class="card" style="left:618px;top:1571px">
    <svg width="48" height="46" viewBox="0 0 48 46" fill="none" stroke="#222" stroke-width="1.6"><path d="M2 40h30M6 40V28h5v12M14 40V20h5v20M22 40V24h5v16"/><circle cx="36" cy="14" r="9"/><path d="M42 21l5 6"/><path d="M8 18l8-8 6 4 8-10"/></svg>
    <h3>SEO And Marketing</h3>
    <p>Lorem Ipsum Is Simply Dummy Text Of The Printing And Typesetting Industry.</p>
    <div class="btn-outline">Read More</div>
  </div>
</section>

<section class="reviews">
  <div class="tick" style="left:599px;top:87px"></div>
  <h2 class="section-title abs" style="left:0;width:1200px;top:122px">Client Reviews</h2>
  <div class="arrow" style="left:90px;top:271px"><svg width="10" height="12" viewBox="0 0 10 12"><path d="M7 1 2 6l5 5" fill="none" stroke="#111" stroke-width="1.6"/></svg></div>
  <div class="arrow" style="left:1075px;top:271px"><svg width="10" height="12" viewBox="0 0 10 12"><path d="M3 1l5 5-5 5" fill="none" stroke="#111" stroke-width="1.6"/></svg></div>
  <div class="review" style="left:135px;top:193px"><div class="face" role="img" aria-label="Client portrait"></div>Lumora Works Provided Us With A High Quality, Functional, Easy To Navigate And Beautiful Website.<div class="who">– J. Carter</div></div>
  <div class="review" style="left:460px;top:193px"><div class="face" role="img" aria-label="Client portrait"></div><div style="margin-top:23px">Lorem Ipsum Is Simply Dummy Text Of The Printing And Typesetting Industry.</div><div class="who">– Daniel R</div></div>
  <div class="review" style="left:783px;top:193px"><div class="face" role="img" aria-label="Client portrait"></div><div style="margin-top:23px">Lorem Ipsum Is Simply Dummy Text Of The Printing And Typesetting Industry.</div><div class="who">– Nora L</div></div>
</section>

<section class="stats">
  <div class="stat" style="left:154px"><b>20</b><span>Employees</span></div>
  <div class="vline" style="left:367px"></div>
  <div class="stat" style="left:380px;top:48px"><b>135</b><span>Customers</span></div>
  <div class="vline" style="left:594px"></div>
  <div class="stat" style="left:613px"><b>45</b><span>New Projects</span></div>
  <div class="vline" style="left:832px"></div>
  <div class="stat" style="left:843px"><b>45k</b><span>Followers</span></div>
</section>

<section class="blog">
  <div class="tick" style="left:599px;top:2617px"></div>
  <h2 class="section-title abs" style="left:0;width:1200px;top:2652px">Latest Blog Posts</h2>
  <div class="arrow" style="left:92px;top:2892px"><svg width="10" height="12" viewBox="0 0 10 12"><path d="M7 1 2 6l5 5" fill="none" stroke="#111" stroke-width="1.6"/></svg></div>
  <div class="arrow" style="left:1077px;top:2892px"><svg width="10" height="12" viewBox="0 0 10 12"><path d="M3 1l5 5-5 5" fill="none" stroke="#111" stroke-width="1.6"/></svg></div>
  <article class="post" style="left:142px"><div class="img" style="background:linear-gradient(135deg,#c8ccd3,#5d6a86 60%,#2d3447)" role="img" aria-label="Person browsing a tablet on a sofa"></div><h4>9 Effective Content Marketing Formats You Need To Know</h4><p>There Are A Variety Of Content Formats Used To Execute Content Marketing Plans...</p><div class="meta">By Lumora Works &nbsp;|&nbsp; June 14, 2022</div><a class="more">Read More</a></article>
  <article class="post" style="left:459px"><div class="img" style="background:linear-gradient(135deg,#1d2230,#3e4a63 50%,#b08a73)" role="img" aria-label="Hands typing on a laptop showing a blog editor"></div><h4>9 Ways To Promote Your Blog On Social Media</h4><p>This Goes Without Saying, But Make Sure You Publish A New Post And Share It On Social Media As Soon As You Can...</p><div class="meta">By Lumora Works &nbsp;|&nbsp; May 17, 2022</div><a class="more">Read More</a></article>
  <article class="post" style="left:776px"><div class="img" style="background:linear-gradient(135deg,#f1f0ec,#d6d3cc 60%,#7a736a)" role="img" aria-label="Team sketching a business mind map on a whiteboard"></div><h4 style="padding-top:3px">Guide To Mind Mapping</h4><p>Mind Mapping Means Brainstorming, And It's A Simple Concept You Can Explore In Both Personal And Corporate Settings...</p><div class="meta">By Lumora Works &nbsp;|&nbsp; April 19, 2022</div><a class="more">Read More</a></article>
  <div class="btn-outline" style="left:540px;top:3186px;width:119px;height:34px">View All Post</div>
</section>

<section class="clients">
  <div class="tick" style="left:599px;top:3310px"></div>
  <h2 class="section-title abs" style="left:0;width:1200px;top:3345px;font-weight:400">Our Clients</h2>
  <div class="client" style="left:154px">Brightpath Learning</div>
  <div class="client" style="left:340px">Harlow Legal</div>
  <div class="client" style="left:526px"><span style="width:14px;height:14px;background:#333;display:inline-block"></span>Kestrel Ventures</div>
  <div class="client" style="left:712px"><span style="width:16px;height:16px;border-radius:50%;background:#bbb;display:inline-block"></span>Keystone Homes</div>
  <div class="client" style="left:898px">Coastal Kitchen</div>
</section>

<footer class="footer">
  <h5 style="left:149px">Quick Links</h5>
  <ul style="left:149px;top:112px"><li>Home</li><li>About Us</li><li>Services</li><li>Blogs</li><li>Contact Us</li></ul>
  <h5 style="left:368px">Contact Details</h5>
  <div class="fitem" style="left:368px;top:116px"><span class="ficon"></span><span>12 Lorem Imsum, Street Name,<br>City Name, Country - 12345</span></div>
  <div class="fitem" style="left:368px;top:172px"><span class="ficon"></span><span><b>Phone</b><br>555-014-2281</span></div>
  <div class="fitem" style="left:368px;top:230px"><span class="ficon"></span><span><b>Email</b><br>hello@lumoraworks.example</span></div>
  <h5 style="left:699px">Follow Us On</h5>
  <div class="fitem" style="left:699px;top:118px;align-items:center"><span class="ficon"></span>Circlebook</div>
  <div class="fitem" style="left:699px;top:180px;align-items:center"><span class="ficon"></span>Chirper</div>
  <div class="fitem" style="left:699px;top:242px;align-items:center"><span class="ficon"></span>Linkwork</div>
  <div class="footer-brand">Lumora Works</div>
  <div class="rule"></div>
  <div class="legal" style="left:142px">© 2024 Lumora Works, LLC. All Rights Reserved.</div>
  <div class="legal" style="right:141px">Privacy Terms Disclaimer.</div>
</footer>

</body>
</html>
```